Bramwell Resources Ltd. - Refreshed business card challenge

A revised, refreshed business card design for my oil and gas company using my existing logo. Feel free to be as creative as you like!

Target Market(s)

bankers, lawyers

Industry/Entity Type

Oil And Gas Exploration

Contact Information for Business Card

See the "Must Haves" section

Font styles to use
Serif
Sans Serif

Colors

Designer to choose colors to be used in the design.

Requirements
Must have
• Existing business logo, name, title, email, phone number, business address
• Neil Hadley, CA, CPA
• Vice President Finance & Chief Financial Officer
• nhadley@bramwellresources-mail.com
• office: (587)555-0142
• cell: (403)555-0187
• 1400, 815 4 Street S.W.
• Calgary, AB
• T2P 4K8
Should not have
• Should not be plain and boring.

```html
<!DOCTYPE html>
<html lang="en">
<head>
<meta charset="utf-8">
<title>Bramwell Resources – Business Card</title>
<link href="https://fonts.googleapis.com/css2?family=Bebas+Neue&family=Montserrat:wght@500;600;800&display=swap" rel="stylesheet">
<style>
  :root {
    --forest: #004a33;
    --bark: #51280a;
    --paper: #ffffff;
    --mist: #f1f1f1;
    --backdrop: #e9e6e1;
  }
  * { margin: 0; padding: 0; box-sizing: border-box; }
  html, body { width: 1200px; height: 1200px; overflow: hidden; }
  body { background: var(--backdrop); position: relative; font-family: "Montserrat", sans-serif; }

  .card {
    position: absolute; top: 460px; width: 480px; height: 281px; overflow: hidden;
    box-shadow: 0 6px 18px rgba(0,0,0,.18);
  }
  .card--front { left: 100px; background: var(--paper); }
  .card--back { left: 620px; background: var(--forest); }

  .front__panel { position: absolute; left: 240px; top: 0; width: 240px; height: 281px; background: var(--mist); }
  .front__base { position: absolute; left: 0; bottom: 0; width: 480px; height: 281px; }

  .wordmark {
    position: absolute; font-family: "Montserrat", sans-serif; font-weight: 800;
    letter-spacing: -0.5px; white-space: nowrap; display: flex; align-items: center; gap: 10px;
  }
  .wordmark__dot { width: 14px; height: 14px; border-radius: 50%; background: currentColor; flex: none; }
  .wordmark__name { display: block; line-height: 1.02; }
  .card--front .wordmark { left: 44px; top: 118px; font-size: 26px; color: var(--forest); }
  .card--back .wordmark { left: 0; width: 480px; justify-content: center; top: 108px; font-size: 30px; color: var(--paper); }

  .holder { position: absolute; left: 254px; top: 38px; width: 206px; text-align: center; }
  .holder__name { font-family: "Bebas Neue", sans-serif; font-size: 31px; font-weight: 400; line-height: 1; color: var(--forest); white-space: nowrap; }
  .holder__title { margin-top: 4px; font-size: 7.2px; font-weight: 500; color: var(--bark); white-space: nowrap; }

  .contacts { position: absolute; left: 255px; top: 118px; width: 218px; list-style: none; }
  .contacts li { display: flex; align-items: flex-start; gap: 8px; font-size: 9.4px; font-weight: 500; color: var(--forest); line-height: 15px; margin-bottom: 5px; white-space: nowrap; }
  .contacts svg { width: 15px; height: 15px; flex: none; }

  .back__band { position: absolute; left: 0; top: 230px; width: 480px; height: 36px;
    background: var(--bark); border-top: 3px solid var(--paper); border-bottom: 3px solid var(--paper); }
  .back__url { position: absolute; left: 0; top: 241px; width: 480px; text-align: center;
    color: var(--paper); font-size: 10.5px; font-weight: 600; letter-spacing: .3px; }
</style>
</head>
<body>
  <section class="card card--front">
    <div class="front__panel"></div>
    <svg class="front__base" viewBox="0 0 480 281" preserveAspectRatio="none" aria-hidden="true">
      <polygon points="0,228 480,224 480,232 0,238" fill="#ececec"/>
      <polygon points="186,264 480,227 480,281 186,281" fill="var(--forest)"/>
      <polygon points="0,236 397,281 0,281" fill="var(--bark)"/>
    </svg>

    <div class="wordmark"><span class="wordmark__dot"></span><span class="wordmark__name">Bramwell<br>Resources</span></div>

    <header class="holder">
      <h1 class="holder__name">Neil Hadley, CA, CPA</h1>
      <p class="holder__title">Vice President Finance &amp; Chief Financial Officer</p>
    </header>

    <ul class="contacts">
      <li>
        <svg viewBox="0 0 16 16"><circle cx="8" cy="8" r="8" fill="var(--forest)"/><rect x="4" y="5.2" width="8" height="5.6" fill="none" stroke="#fff" stroke-width="1"/><path d="M4 5.5 8 8.6 12 5.5" fill="none" stroke="#fff" stroke-width="1"/></svg>
        <span>nhadley@bramwellresources-mail.com</span>
      </li>
      <li>
        <svg viewBox="0 0 16 16"><circle cx="8" cy="8" r="8" fill="var(--bark)"/><path d="M4 7.2c0-1.6 8-1.6 8 0v.8h-2v-.8H6v.8H4z M5.5 8.5h5l.8 3H4.7z" fill="#fff"/></svg>
        <span>(587)555-0142</span>
      </li>
      <li>
        <svg viewBox="0 0 16 16"><circle cx="8" cy="8" r="8" fill="var(--forest)"/><rect x="5.5" y="3.5" width="5" height="9" rx="1" fill="none" stroke="#fff" stroke-width="1"/><circle cx="8" cy="11" r=".6" fill="#fff"/></svg>
        <span>(403)555-0187</span>
      </li>
      <li>
        <svg viewBox="0 0 16 16"><circle cx="8" cy="8" r="8" fill="var(--bark)"/><path d="M8 3.2a3 3 0 0 1 3 3c0 2.2-3 6-3 6s-3-3.8-3-6a3 3 0 0 1 3-3z" fill="#fff"/><circle cx="8" cy="6.2" r="1.1" fill="var(--bark)"/></svg>
        <span>1400, 815 4 Street S.W.<br>Calgary, AB<br>T2P 4K8</span>
      </li>
    </ul>
  </section>

  <section class="card card--back">
    <div class="wordmark"><span class="wordmark__dot"></span>Bramwell Resources</div>
    <div class="back__band"></div>
    <p class="back__url">www.bramwellresources-web.com</p>
  </section>
</body>
</html>
```